High Quality fast food restaurant - Tomanyo

Tomanyo is a fast food company with its target's focused on logistic, simplicity, high quality, freshness and modern.

We need a web design where the customers can get a complete idea of our high quality completeness, we want to take fast food to a new upper level.

We would like to see the colours of wood and metal. Pictures have been attached of our local.

We would like to have something in similar to: http://www.qpz.example/
Updates

Images for the food we are going to sell can be found here: http://shrt.example/uWQa7

It will be the images with rice, french fries or pita bread.

Target Market(s)

The fast food eating people between sloppy food and restaurant level.

Industry/Entity Type

Fast Food Restaurant

Requirements
Should not have
• No Flash or Java

```html
<!DOCTYPE html>
<html lang="en">
<head>
<meta charset="utf-8">
<title>Tomanyo – High Quality Fast Food</title>
<link href="https://fonts.googleapis.com/css2?family=Arvo:wght@400;700&family=Ubuntu:wght@400;500;700&display=swap" rel="stylesheet">
<style>
:root{
  --brown-dark:#2a150d;
  --brown:#3a2116;
  --gold:#c08a22;
  --gold-light:#e2b43a;
  --cream:#f1e6d2;
  --paper:#f4efe6;
  --red:#d8232a;
  --text:#9a8f80;
  --ink:#1d1410;
  --white:#ffffff;
}
*{margin:0;padding:0;box-sizing:border-box}
html,body{width:1081px;height:1200px;overflow:hidden;background:var(--paper)}
body{position:relative;font-family:"Ubuntu",sans-serif}
.abs{position:absolute}

.site-header{left:0;top:0;width:1081px;height:84px;background:linear-gradient(#3b2216,var(--brown-dark))}
.brand{left:113px;top:18px;font-family:"Arvo",serif;font-weight:700;font-size:44px;color:var(--white);letter-spacing:1px}
.support-icon{left:763px;top:20px}
.support-label{left:812px;top:20px;font-size:13px;color:var(--gold-light)}
.support-phone{left:811px;top:34px;font-size:22px;color:var(--white);letter-spacing:1px}

.hero{left:0;top:84px;width:1081px;height:557px;background:
  radial-gradient(ellipse at 55% 35%,rgba(255,240,220,.45),transparent 60%),
  linear-gradient(100deg,#8a6048 0%,#b99078 35%,#a7785c 65%,#6d4431 100%)}
.main-nav{left:109px;top:84px;width:865px;height:34px;background:linear-gradient(#e0b546,#c3921f);display:flex;align-items:center;box-shadow:0 2px 4px rgba(0,0,0,.3)}
.main-nav a{display:flex;align-items:center;justify-content:center;height:34px;color:var(--white);font-weight:500;font-size:12.5px;text-decoration:none;border-right:1px solid rgba(120,80,10,.5)}
.main-nav a:last-of-type{border-right:none}
.follow{margin-left:auto;display:flex;align-items:center;gap:6px;padding-right:8px;color:var(--white);font-weight:500;font-size:13px}
.follow span{margin-right:16px}
.social-dot{width:23px;height:23px;border-radius:50%;background:#1f5fa8;border:2px solid #e8c45a}

.hero-copy{left:117px;top:178px;font-family:"Arvo",serif;font-weight:700;color:var(--ink);line-height:36px;font-size:33px}
.hero-copy .gold{color:var(--gold)}
.hero-copy .from{font-weight:400;font-size:30px;margin-top:6px}
.hero-copy .price{color:var(--white);font-size:46px;font-weight:700}
.hero-copy sup{font-size:16px;color:var(--white);vertical-align:26px}
.hero-intro{left:117px;top:362px;font-family:"Arvo",serif;font-size:16.5px;line-height:21px;color:var(--white)}
.order-btn{left:115px;top:424px;width:139px;height:37px;border-radius:8px;background:var(--brown-dark);color:var(--white);font-family:"Arvo",serif;font-size:17px;display:flex;align-items:center;justify-content:center}
.food-rice{left:425px;top:165px;width:310px;height:205px;border-radius:40% 40% 48% 48%;background:radial-gradient(ellipse at 50% 35%,#e9c35a,#d88a3a 55%,#f4f2ee 75%)}
.food-fries{left:308px;top:440px;width:355px;height:185px;border-radius:20%;background:radial-gradient(ellipse at 50% 50%,#d9692a,#e08a45 50%,#f3efea 75%)}
.food-pita{left:678px;top:288px;width:324px;height:347px;border-radius:45%;background:radial-gradient(ellipse at 45% 30%,#f2d2a8,#e2b88a 60%,#d0a070)}

.welcome{left:0;top:641px;width:1081px;height:230px;background:linear-gradient(90deg,#efe1c8,#f6ecdb 50%,#ecdcc2)}
.welcome-title{left:116px;top:678px;font-size:30px;font-weight:500;color:var(--gold)}
.welcome-text{left:116px;top:719px;width:530px;font-size:12.5px;line-height:19.5px;color:var(--text)}
.welcome-text p+p{margin-top:19px}
.video{left:666px;top:690px;width:306px;height:152px;border-radius:4px;background:linear-gradient(#5a4033,#2b1d17);overflow:hidden;box-shadow:0 2px 4px rgba(0,0,0,.4)}
.video-still{position:absolute;left:0;top:0;width:306px;height:118px;background:radial-gradient(ellipse at 40% 50%,#d8c9c0,#6b4a38 60%,#2b1d17)}
.video-bar{position:absolute;left:0;bottom:0;width:306px;height:34px;background:#1b1411;display:flex;align-items:center;padding:0 10px;gap:10px}
.play{width:20px;height:20px;background:var(--gold);border-radius:3px}
.track{flex:1;height:5px;background:#ddd;border-radius:3px;position:relative}
.track i{position:absolute;left:0;top:0;width:60px;height:5px;background:#777;border-radius:3px}

.newsletter{left:0;top:871px;width:1081px;height:49px;background:var(--red);color:var(--white);font-size:16px;font-weight:500}
.newsletter-label{position:absolute;left:115px;top:15px;white-space:nowrap}
.newsletter-input{position:absolute;left:320px;top:14px;width:281px;height:21px;background:var(--white)}
.newsletter-submit{position:absolute;left:601px;top:14px;width:75px;height:21px;background:#4a2a1a;color:var(--gold-light);font-size:16px;display:flex;align-items:center;justify-content:center}
.like-label{position:absolute;right:150px;top:15px;white-space:nowrap}
.like-icon{position:absolute;left:940px;top:11px;width:26px;height:26px;background:#3d5b98;border-radius:3px}

.card{top:945px;width:282px;height:177px;border-radius:6px;border:1px solid #cfcfcf;background:linear-gradient(#ffffff,#e4e4e4);padding:0 10px}
.card h3{font-size:14.5px;font-weight:500;color:var(--ink);margin:12px 0 5px 4px}
.card-media{height:68px;border:1px solid #ccc}
.card p{font-size:9.5px;line-height:16px;color:#777;margin:7px 2px}
.media-map{background:linear-gradient(135deg,#f3f0e4,#dcdcdc 50%,#f1edd8)}
.media-takeaway{background:linear-gradient(180deg,#f8f4ee,#efd9b8)}

.customers-title{left:768px;top:947px;font-size:14.5px;font-weight:700;color:var(--ink)}
.quote{left:767px;top:970px;width:196px;height:137px;background:#b98a1f;color:var(--white);font-size:10.5px;line-height:16.2px;padding:22px 18px}
.quote cite{display:block;font-style:normal;margin-top:8px}
.quote-tail{left:863px;top:1106px}
.dots{left:928px;top:1117px;display:flex;gap:5px}
.dots i{width:8px;height:8px;border-radius:50%;background:#999}
.dots i:first-child{background:var(--gold)}

.site-footer{left:0;top:1146px;width:1081px;height:54px;background:var(--brown-dark);color:var(--white);font-size:11px}
.copyright{position:absolute;left:115px;top:22px;font-family:Arial,sans-serif}
.footer-nav{position:absolute;right:117px;top:21px;display:flex;gap:17px}
.footer-nav a{color:var(--white);text-decoration:none;font-size:11px}
</style>
</head>
<body>

<header class="abs site-header"></header>
<div class="abs brand">TOMANYO</div>
<svg class="abs support-icon" width="40" height="44" viewBox="0 0 40 44" aria-hidden="true">
  <path d="M6 24 V18 A14 14 0 0 1 34 18 V24" fill="none" stroke="#bbb" stroke-width="3"/>
  <rect x="3" y="21" width="8" height="13" rx="3" fill="#ddd"/>
  <rect x="29" y="21" width="8" height="13" rx="3" fill="#ddd"/>
  <path d="M7 34 Q8 42 18 42" fill="none" stroke="#bbb" stroke-width="2"/>
</svg>
<div class="abs support-label">24/7 Online Support Service</div>
<div class="abs support-phone">1-800-555-0147</div>

<section class="abs hero"></section>
<nav class="abs main-nav">
  <a style="width:71px">HOME</a>
  <a style="width:94px">SERVICES</a>
  <a style="width:97px">ABOUT US</a>
  <a style="width:68px">MENU</a>
  <a style="width:122px">ONLINE ORDER</a>
  <a style="width:83px">TIMINGS</a>
  <a style="width:107px">CONTACT US</a>
  <div class="follow"><span>Follow Us</span><i class="social-dot"></i><i class="social-dot"></i><i class="social-dot" style="background:#1ea1d8"></i></div>
</nav>

<div class="abs food-rice" role="img" aria-label="White bowl of vegetable fried rice"></div>
<div class="abs food-fries" role="img" aria-label="Paper tray of seasoned french fries"></div>
<div class="abs food-pita" role="img" aria-label="Stack of fresh pita breads"></div>

<div class="abs hero-copy">
  <div>LARGE</div>
  <div class="gold">Pita Breads With</div>
  <div>Rice &amp; Fries</div>
  <div class="from">starting from <span class="price">4.5</span><sup>$</sup></div>
</div>
<div class="abs hero-intro">INTRODUCING IMPROVED QUALITY<br>BETTER-THEN-EVER.</div>
<div class="abs order-btn">ORDER NOW</div>

<section class="abs welcome"></section>
<h1 class="abs welcome-title">Welcome To Tomanyo</h1>
<div class="abs welcome-text">
  <p>Lorem Ipsum is simply dummy text of the printing and typesetting industry. Lorem Ipsum has been the industry's standard dummy text ever since the 1500s, when an unknown printer took a galley of type and scrambled it to make a type specimen book.</p>
  <p>Lorem Ipsum is simply dummy text of the printing and typesetting industry. Lorem Ipsum has been the industry's standard dummy text ever since the 1500s,</p>
</div>
<div class="abs video">
  <div class="video-still" role="img" aria-label="Video still of a shawarma plate with salad and fries"></div>
  <div class="video-bar"><i class="play"></i><div class="track"><i></i></div>
    <svg width="44" height="14" viewBox="0 0 44 14" aria-hidden="true"><rect x="0" y="9" width="3" height="5" fill="#c08a22"/><rect x="5" y="7" width="3" height="7" fill="#c08a22"/><rect x="10" y="4" width="3" height="10" fill="#c08a22"/><rect x="15" y="1" width="3" height="13" fill="#777"/><path d="M33 2h3M33 2v3M43 2h-3M43 2v3M33 12h3M33 12v-3M43 12h-3M43 12v-3" stroke="#ddd" stroke-width="1.5"/></svg>
  </div>
</div>

<div class="abs newsletter">
  <span class="newsletter-label">SIGNUP FOR NEWSLETTER</span>
  <span class="newsletter-input"></span>
  <span class="newsletter-submit">SUBMIT</span>
  <span class="like-label">LIKE US ON FRIENDWALL</span>
  <span class="like-icon"></span>
</div>

<article class="abs card" style="left:123px">
  <h3>Find Tomanyo Near You</h3>
  <div class="card-media media-map" role="img" aria-label="Street map showing nearby locations"></div>
  <p>Lorem Ipsum is simply dummy text of the printing and typesetting industry. Lorem Ipsum has been the industry's standard dummy text ever since the 1500s,</p>
</article>
<article class="abs card" style="left:446px">
  <h3>Online Order</h3>
  <div class="card-media media-takeaway" role="img" aria-label="Takeaway ordering banner"></div>
  <p>Lorem Ipsum is simply dummy text of the printing and typesetting industry. Lorem Ipsum has been the industry's standard dummy text ever since the 1500s,</p>
</article>

<h3 class="abs customers-title">Our Happy Customers</h3>
<blockquote class="abs quote">“Lorem ipsum dolor sit amet, consectetur adipisicing elit, sed do eiusmod tempor incididunt ut labore et dolore magna aliqua. Ut enim ad minim veniam.”<cite>Mr. Lorem Ipsum</cite></blockquote>
<svg class="abs quote-tail" width="36" height="26" viewBox="0 0 36 26" aria-hidden="true"><path d="M0 0 H36 L33 26 Z" fill="#b98a1f"/></svg>
<div class="abs dots"><i></i><i></i><i></i></div>

<footer class="abs site-footer">
  <div class="copyright">© Copyright Tomanyo 2013</div>
  <nav class="footer-nav"><a>Home</a><a>Services</a><a>About Us</a><a>Menu</a><a>Online Order</a><a>Timings</a><a>Contact us</a></nav>
</footer>

</body>
</html>
```